"Rise. Shift. Thrive." Empowerment Book Cover

Hello, I need a hot, trendy, and contemporary book cover designed for my first book called "Rise. Shift. Thrive. -- 360 Bold Momentum Notes to Guide Anyone to Rise, Shift, and Thrive in Their Career & Daily Dreams."
This is my first book and I am really wanting to launch my brand with it... it would be awesome to match the inside/outside branding of the book. So we can either create the book cover to match the book guts, or update the book guts to match the cover.
Lastly, I just got a professional photoshoot done last week so we can use one of those images, or we can go with a different idea/style for the cover. The body of the book is attached. All questions welcomed, happy designing!
Target Market(s)
Gen Z, Millennials and Gen X.
Industry/Entity Type
Personal Development.
Requirements
Must have
- It must stand out and be different from other typical book covers.
Nice to have
- Success, Inspiration, Motivation, Mindset, Growth.
Should not have
- Clipart, stock art, stock look and feel.

```html
<!DOCTYPE html>
<html lang="en">
<head>
<meta charset="utf-8">
<title>Rise. Shift. Thrive. — Book Cover</title>
<link href="https://fonts.googleapis.com/css2?family=Questrial&family=Poppins:wght@600&display=swap" rel="stylesheet">
<style>
  :root {
    --cover-blue: #0151ae;
    --band-blue: rgba(40, 140, 215, 0.55);
    --title-light: #6cc8ec;
    --title-main: #00a1df;
    --title-shade: #0a3f9a;
    --white: #ffffff;
    --portrait-light: #b9bcc1;
    --portrait-dark: #8d9097;
  }
  html, body {
    margin: 0;
    padding: 0;
    width: 799px;
    height: 1200px;
    overflow: hidden;
    background: var(--cover-blue);
  }
  .cover {
    position: relative;
    width: 799px;
    height: 1200px;
    background: var(--cover-blue);
    overflow: hidden;
    font-family: "Questrial", sans-serif;
    color: var(--white);
  }
  .portrait {
    position: absolute;
    left: 0;
    top: 0;
    width: 799px;
    height: 1200px;
  }
  .website {
    position: absolute;
    right: 33px;
    top: 36px;
    font-size: 19px;
    letter-spacing: 0.5px;
  }
  .title {
    position: absolute;
    left: 50px;
    top: 232px;
    margin: 0;
    font-weight: 400;
    font-size: 172px;
    line-height: 183px;
    letter-spacing: -2px;
  }
  .title span { display: block; }
  .title .line-one { color: var(--title-light); text-shadow: 3px 3px 0 #3a9bd6; }
  .title .line-two,
  .title .line-three { color: var(--title-main); text-shadow: 3px 3px 0 var(--title-shade); }
  .subtitle-band {
    position: absolute;
    left: 0;
    top: 772px;
    width: 799px;
    height: 154px;
    background: var(--band-blue);
  }
  .subtitle {
    position: absolute;
    left: 55px;
    top: 783px;
    margin: 0;
    font-family: "Poppins", sans-serif;
    font-weight: 600;
    font-size: 28px;
    line-height: 44px;
    letter-spacing: -0.3px;
  }
  .subtitle span { display: block; }
  .author {
    position: absolute;
    left: 0;
    width: 799px;
    top: 1052px;
    text-align: center;
  }
  .author-name {
    display: block;
    font-size: 64px;
    line-height: 66px;
    letter-spacing: 1px;
    padding-left: 22px;
  }
  .author-role {
    display: block;
    font-size: 30px;
    line-height: 36px;
    margin-top: 2px;
    padding-left: 22px;
  }
</style>
</head>
<body>
  <main class="cover">
    <svg class="portrait" viewBox="0 0 799 1200" role="img" aria-label="Author photo: smiling bearded man in glasses and a light grey suit, hands in pockets">
      <defs>
        <linearGradient id="suit" x1="0" y1="0" x2="1" y2="1">
          <stop offset="0" stop-color="var(--portrait-light)"/>
          <stop offset="1" stop-color="var(--portrait-dark)"/>
        </linearGradient>
      </defs>
      <path d="M310 20 Q390 -5 470 25 L485 220 Q610 260 660 330 L690 620 L640 960 L580 1200 L250 1200 L215 960 L190 620 L215 320 Q260 250 320 225 Z" fill="url(#suit)"/>
    </svg>

    <div class="website">www.MomentumShiftLab.com</div>

    <h1 class="title">
      <span class="line-one">Rise.</span>
      <span class="line-two">Shift.</span>
      <span class="line-three">Thrive.</span>
    </h1>

    <div class="subtitle-band"></div>
    <p class="subtitle">
      <span>360 Bold Momentum Notes</span>
      <span>to Guide Anyone to Rise, Shift, and Thrive</span>
      <span>in Their Career &amp; Daily Dreams.</span>
    </p>

    <div class="author">
      <span class="author-name">Darian Kole</span>
      <span class="author-role">Momentum Coach</span>
    </div>
  </main>
</body>
</html>
```